Masonry company / pouring concrete / decorative concrete recherche Flyer

We need a Flyer creation to advertise our company called "Ridgeline Concrete". We are a company specializing in decorative concrete / decorative concrete for outdoor landscaping (terraces, patio, driveway etc ...) We want a Flyer size A5 (21cm / 14.8cm) Recto-Verso. Which attracts the eye and especially that shows the different products that we offer (printed concrete / miccrochape / washed concrete / masonry / luminescent concrete / sanitation / earthwork) Our Logo should be recalled and the Flyer must be in the same colors as the logo (white and / or black) and with the same design as the logo (squares).

Target Market(s)

25-80 years

Industry/Entity Type

Concrete

Colors
f78f20
000000
ffffff
9d9d9d

Requirements
Must have
• Logo / photos (even other than those proposed but still on printed concrete) / double-sided /
Nice to have
• It would be nice if the way the flyer is designed, reminds the shape of the logo. For example that the images are arranged like the small squares and rectangles of the logo. It would be nice to have the motif "wood" in the background of the flyer.
Should not have
• You can use the "nameless" file but do not copy it.

```html
<!DOCTYPE html>
<html lang="en">
<head>
<meta charset="utf-8">
<title>Ridgeline Concrete Flyer</title>
<link href="https://fonts.googleapis.com/css2?family=Montserrat:wght@600&family=Questrial&display=swap" rel="stylesheet">
<style>
  :root {
    --orange: #f78f20;
    --board: #2b2b2b;
    --board-light: #353535;
    --frame-grey: #8a8a8a;
    --text-white: #ffffff;
    --text-grey: #c4c4c4;
    --rule: #5a5a5a;
    --page: #ececec;
  }
  * { margin: 0; padding: 0; box-sizing: border-box; }
  html, body { width: 1200px; height: 1200px; overflow: hidden; background: var(--page); }
  .flyer {
    position: absolute; left: 191px; top: 20px; width: 818px; height: 1160px;
    background: linear-gradient(160deg, var(--board-light) 0%, var(--board) 45%, #262626 100%);
    font-family: "Questrial", sans-serif;
  }
  .brand {
    position: absolute; left: 86px; top: 104px; width: 290px;
    display: flex; flex-direction: column; align-items: center; gap: 18px;
  }
  .brand-square { width: 64px; height: 64px; background: var(--orange); }
  .brand-name { font-family: "Questrial", sans-serif; font-size: 36px; color: var(--orange); white-space: nowrap; }
  .photo { position: absolute; border: 3px solid var(--frame-grey); }
  .photo.accent { border-color: var(--orange); }
  .photo-driveway-top { left: 426px; top: 53px; width: 338px; height: 143px;
    background: linear-gradient(180deg, #6d6d6d 0%, #c9c9c9 40%, #e2e2e2 100%); }
  .photo-cobble { left: 54px; top: 233px; width: 339px; height: 339px;
    background: linear-gradient(180deg, #f2f2f2 0%, #3a3a3a 30%, #a8a8a8 45%, #d6d6d6 100%); }
  .photo-spray { left: 426px; top: 233px; width: 338px; height: 339px;
    background: linear-gradient(135deg, #e9e4ea 0%, #c8a98a 40%, #b8232d 60%, #d9c3b0 100%); }
  .photo-garage { left: 54px; top: 615px; width: 339px; height: 338px;
    background: linear-gradient(180deg, #e8e4dc 0%, #d9dcdc 50%, #8c1c33 68%, #a82443 100%); }
  .photo-lane { left: 426px; top: 615px; width: 338px; height: 338px;
    background: linear-gradient(180deg, #e9eee6 0%, #4c6b34 35%, #6f8a4a 55%, #d8cdb8 75%, #e6ddcc 100%); }
  .services { position: absolute; left: 54px; top: 972px; list-style: none; }
  .services li {
    display: flex; align-items: center; height: 35.5px;
    font-family: "Montserrat", sans-serif; font-weight: 600; font-size: 23px; color: var(--text-white);
  }
  .services li.muted { color: var(--text-grey); }
  .services .bullet { width: 17px; height: 17px; border: 3px solid var(--orange); margin-right: 18px; flex: none; }
  .contact { position: absolute; left: 513px; top: 974px; width: 251px; }
  .contact-title { font-size: 17px; color: var(--text-white); padding-bottom: 6px; border-bottom: 1px solid var(--rule); margin-bottom: 6px; }
  .contact-row { display: flex; align-items: center; height: 25.5px; font-size: 17px; color: var(--text-white); white-space: nowrap; }
  .contact-row.phone { font-family: "Montserrat", sans-serif; font-weight: 600; font-size: 18px; }
  .contact-row svg { width: 19px; height: 19px; margin-right: 10px; flex: none; }
  .bottom-rule { position: absolute; left: 54px; right: 54px; top: 1130px; height: 1px; background: var(--rule); }
</style>
</head>
<body>
  <main class="flyer">
    <div class="brand">
      <div class="brand-square"></div>
      <div class="brand-name">Ridgeline Concrete</div>
    </div>

    <div class="photo photo-driveway-top" role="img" aria-label="Grey concrete driveway between hedges"></div>
    <div class="photo photo-cobble" role="img" aria-label="Courtyard paved with printed cobblestone concrete"></div>
    <div class="photo photo-spray accent" role="img" aria-label="Red spray gun in front of coloured concrete samples"></div>
    <div class="photo photo-garage accent" role="img" aria-label="Basement with red resin-coated concrete floor"></div>
    <div class="photo photo-lane" role="img" aria-label="Washed concrete lane lined with trees"></div>

    <ul class="services">
      <li><span class="bullet"></span>Maconnerie</li>
      <li class="muted"><span class="bullet"></span>Beton Decoriatifs</li>
      <li><span class="bullet"></span>Coloration des sols betons</li>
      <li class="muted"><span class="bullet"></span>Terrasement&nbsp; Assainissement</li>
    </ul>

    <div class="contact">
      <div class="contact-title">Contact details :</div>
      <div class="contact-row phone">
        <svg viewBox="0 0 24 24" fill="var(--orange)"><path d="M6.6 10.8c1.4 2.8 3.8 5.1 6.6 6.6l2.2-2.2c.3-.3.7-.4 1-.2 1.1.4 2.3.6 3.6.6.6 0 1 .4 1 1V20c0 .6-.4 1-1 1C10.6 21 3 13.4 3 4c0-.6.4-1 1-1h3.5c.6 0 1 .4 1 1 0 1.3.2 2.5.6 3.6.1.3 0 .7-.2 1z"/></svg>
        33 6 41 27 58 04
      </div>
      <div class="contact-row">
        <svg viewBox="0 0 24 24" fill="var(--orange)"><path d="M12 3 2 12h3v9h5v-6h4v6h5v-9h3z"/></svg>
        22410 Kervalen
      </div>
      <div class="contact-row">
        <svg viewBox="0 0 24 24" fill="none" stroke="var(--orange)" stroke-width="2"><rect x="3" y="6" width="18" height="13"/><path d="M3 6l9 7 9-7"/></svg>
        ridgelineconcrete@mail.com
      </div>
      <div class="contact-row">
        <svg viewBox="0 0 24 24" fill="none" stroke="var(--orange)" stroke-width="2"><circle cx="12" cy="12" r="9"/><path d="M3 12h18M12 3c3 3 3 15 0 18M12 3c-3 3-3 15 0 18"/></svg>
        www.ridgelineconcrete.com
      </div>
    </div>

    <div class="bottom-rule"></div>
  </main>
</body>
</html>
```